Evergold Fernbark Inc

Industry/Entity Type

Forestry

Contact Information for Business Card

Company name: Evergold Fernbark INC, Contact Info: Rovelio Marquin, Phone # 912 555 0187, Addres: 284 Willowbend Creek Rd, Larkfield GA 31099, Email: evergoldfernbark@mailbrook.net

```html
<!DOCTYPE html>
<html lang="en">
<head>
<meta charset="utf-8">
<title>Evergold Fernbark INC – Business Card</title>
<link href="https://fonts.googleapis.com/css2?family=Questrial&family=Open+Sans:wght@400&display=swap" rel="stylesheet">
<style>
  :root {
    --page-bg: #e9e8ee;
    --sky-top: #d2d3e9;
    --sky-mid: #c1c2e5;
    --sky-low: #b4b5e0;
    --forest-dark: #7f8283;
    --forest-soft: #9a9ca8;
    --rule: #e6e7f5;
    --ink: #111114;
    --icon-bg: #ffffff;
    --icon-ink: #b4b5e0;
  }
  * { box-sizing: border-box; margin: 0; padding: 0; }
  html, body { width: 1200px; height: 1200px; overflow: hidden; }
  body { background: var(--page-bg); position: relative; }

  .card {
    position: absolute;
    left: 174px;
    width: 896px;
    height: 498px;
    border-radius: 0 48px 0 48px;
    overflow: hidden;
    background: linear-gradient(180deg, var(--sky-top) 0%, var(--sky-mid) 40%, var(--sky-low) 100%);
    box-shadow: 0 6px 14px rgba(0,0,0,0.25);
  }
  .card--front { top: 56px; }
  .card--back { top: 621px; }

  .scene { position: absolute; }
  .scene--mountains {
    left: 0; width: 896px;
    background: linear-gradient(180deg, rgba(160,162,210,0) 0%, rgba(160,162,210,0.55) 50%, rgba(180,181,224,0) 100%);
  }
  .card--front .scene--mountains { top: 110px; height: 180px; }
  .card--back .scene--mountains { top: 100px; height: 200px; }

  .scene--forest {
    top: 40px; height: 458px;
    -webkit-mask-image: linear-gradient(180deg, transparent 0%, #000 30%);
    mask-image: linear-gradient(180deg, transparent 0%, #000 30%);
  }
  .card--front .scene--forest {
    left: 0; width: 410px;
    background: linear-gradient(90deg, var(--forest-dark) 0%, var(--forest-soft) 55%, rgba(180,181,224,0) 100%);
  }
  .card--back .scene--forest {
    left: 0; width: 896px;
    background: linear-gradient(90deg, var(--forest-dark) 0%, var(--forest-soft) 26%, rgba(180,181,224,0) 42%, rgba(180,181,224,0) 62%, var(--forest-soft) 78%, var(--forest-dark) 100%);
  }

  .rule { position: absolute; height: 1px; background: var(--rule); }
  .card--front .rule { left: 380px; right: 0; top: 290px; }
  .card--back .rule--top { left: 0; right: 48px; top: 101px; }
  .card--back .rule--bottom { left: 370px; width: 260px; top: 387px; }

  .contact {
    position: absolute; right: 49px; top: 315px;
    text-align: right; color: var(--ink);
  }
  .contact__name {
    font-family: "Questrial", sans-serif;
    font-size: 58px; font-weight: 400; line-height: 64px; letter-spacing: -0.5px;
  }
  .contact__line {
    display: flex; justify-content: flex-end; align-items: center; gap: 6px;
    font-family: "Open Sans", sans-serif;
  }
  .contact__line--email { font-size: 25px; line-height: 36px; margin-top: 2px; }
  .contact__line--phone { font-size: 34px; line-height: 44px; margin-top: 2px; }
  .icon { width: 20px; height: 20px; flex: none; }

  .company {
    position: absolute; left: 0; right: 0; top: 124px;
    text-align: center; padding-left: 20px;
    font-family: "Questrial", sans-serif; font-size: 57px; font-weight: 400; line-height: 66px;
    color: var(--ink); letter-spacing: -0.5px;
  }
  .address {
    position: absolute; left: 0; right: 0; top: 218px;
    text-align: center; padding-left: 36px;
    font-family: "Questrial", sans-serif; font-size: 29px; line-height: 37px;
    color: var(--ink); font-style: normal;
  }
</style>
</head>
<body>
  <section class="card card--front">
    <div class="scene scene--mountains" role="img" aria-label="Misty mountain range illustration"></div>
    <div class="scene scene--forest" role="img" aria-label="Pine forest silhouette illustration"></div>
    <div class="rule"></div>
    <div class="contact">
      <h1 class="contact__name">Rovelio Marquin</h1>
      <p class="contact__line contact__line--email">
        <svg class="icon" viewBox="0 0 20 20" aria-hidden="true">
          <rect x="0" y="0" width="20" height="20" rx="4" fill="var(--icon-bg)"/>
          <rect x="4" y="6" width="12" height="9" rx="1" fill="var(--icon-ink)"/>
          <path d="M4.5 6.5 L10 11 L15.5 6.5" fill="none" stroke="var(--icon-bg)" stroke-width="1.3"/>
        </svg>
        evergoldfernbark@mailbrook.net
      </p>
      <p class="contact__line contact__line--phone">
        <svg class="icon" viewBox="0 0 20 20" aria-hidden="true">
          <rect x="0" y="0" width="20" height="20" rx="4" fill="var(--icon-bg)"/>
          <path d="M6.5 4.5 L8.5 7.5 L7.4 8.8 C8.2 10.6 9.4 11.8 11.2 12.6 L12.5 11.5 L15.5 13.5 L14.3 15.4 C10 15.6 4.4 10 4.6 5.7 Z" fill="var(--icon-ink)"/>
        </svg>
        912 555 0187
      </p>
    </div>
  </section>

  <section class="card card--back">
    <div class="scene scene--mountains" role="img" aria-label="Misty mountain range illustration"></div>
    <div class="scene scene--forest" role="img" aria-label="Pine forest framing both sides illustration"></div>
    <div class="rule rule--top"></div>
    <h2 class="company">Evergold Fernbark INC</h2>
    <address class="address">
      284 Willowbend<br>
      Creek Rd,<br>
      Larkfield GA<br>
      31099
    </address>
    <div class="rule rule--bottom"></div>
  </section>
</body>
</html>
```